Hello - we need a label design for our Quillon Health Hair Loss supplement. It is a natural hair loss supplement for black/african american women to regrow new hair and help restore hair loss & thinning hair due to vitamin deficiencies, traction alopecia, etc. It is a science based efficacious supplement with a centuries old medicinal herbal formula.
Attached is the logo & files of other generic competition and also Black hair products for your perusal. The label has to be a upscale and have an ethnic flair to it. The product is clinically effective, leveraged by Ancient Wisdom and Modern Science. The front of the label should include the following:
Quillon Health (logo)
Growth Accelerator
Advanced Women’s Hair Loss Formula
TRACTION ALOPECIA THERAPY
- Prevents hair loss & restores thinning, fragile hair
- Promotes Natural Hair Growth
- Strengthens Hair for less breakage
- Visibly increases hair density & thickness
- Thicker, Stronger, Longer, Hydrated hair
- Promotes Follicle regeneration & Hair Growth
Site-Specific for hair loss & stunted growth
60 capsules 30-day supply
Target Market(s)
Black/African American Women
Look and feel

```html
<!DOCTYPE html>
<html lang="en">
<head>
<meta charset="utf-8">
<title>Quillon Health – Growth Accelerator Label</title>
<link rel="stylesheet" href="https://fonts.googleapis.com/css2?family=Josefin+Sans:wght@300;400&family=Fredoka:wght@600&family=Encode+Sans+Condensed:wght@400;600&family=Montserrat:wght@500;700&family=Archivo:wght@400;700;900&display=swap">
<style>
  :root {
    --bg: #f4f2ef;
    --ink: #1d1a18;
    --cream: #f3e7bf;
    --sand: #d9bf8c;
    --tan: #b98a63;
    --bronze: #8a5a3a;
    --white: #ffffff;
    --rule: #2b2522;
    --back-text: #4a4036;
    --badge: #2a2522;
  }
  * { box-sizing: border-box; margin: 0; padding: 0; }
  html, body { width: 1200px; height: 900px; overflow: hidden; background: var(--bg); }
  .label-strip {
    position: absolute; left: 30px; top: 215px;
    width: 1140px; height: 470px;
    display: flex;
    box-shadow: 0 10px 30px rgba(0,0,0,.12);
  }
  .panel { position: relative; width: 380px; height: 470px; overflow: hidden; }

  /* Back panel */
  .panel-back {
    background: linear-gradient(90deg, var(--cream) 0%, #efe2b9 60%, var(--sand) 100%);
  }
  .panel-back .top-band { position: absolute; left: 0; top: 0; width: 100%; height: 48px; background: var(--white); border-bottom: 3px solid var(--rule); }
  .back-headline { position: absolute; left: 24px; top: 86px; font: 700 19px "Montserrat", sans-serif; color: #6b5d4c; }
  .back-copy { position: absolute; left: 22px; width: 345px; font: 500 10.6px/15px "Montserrat", sans-serif; color: var(--back-text); }
  .back-copy.one { top: 126px; }
  .back-copy.two { top: 226px; }
  .info-box { position: absolute; left: 20px; top: 346px; width: 150px; height: 86px; background: #3d3d3d; }
  .badges { position: absolute; left: 200px; top: 330px; display: grid; grid-template-columns: 80px 80px; row-gap: 8px; }
  .badge { display: flex; flex-direction: column; align-items: center; gap: 3px; font: 400 10px "Encode Sans Condensed", sans-serif; color: var(--ink); }
  .badge-mark { width: 34px; height: 34px; border-radius: 50%; border: 2.5px solid var(--badge); }
  .badge-mark.solid { background: var(--badge); }

  /* Front panel */
  .panel-front {
    background: linear-gradient(115deg, #efe0b2 0%, #e2c79a 35%, #c99f76 65%, var(--tan) 100%);
  }
  .front-shapes { position: absolute; inset: 0; }
  .brand { position: absolute; left: 0; top: 38px; width: 330px; display: flex; justify-content: center; align-items: center; gap: 8px; }
  .brand-dot { width: 10px; height: 10px; border-radius: 50%; background: var(--bronze); }
  .brand-name { font: 400 24px "Josefin Sans", sans-serif; color: var(--bronze); letter-spacing: 1px; }
  .eyebrow { position: absolute; left: 22px; top: 134px; font: 300 20px "Josefin Sans", sans-serif; letter-spacing: 3.4px; color: var(--ink); }
  .rule { position: absolute; left: 22px; height: 1px; background: var(--rule); }
  .product-title { position: absolute; left: 22px; top: 162px; font: 600 29px/33px "Fredoka", sans-serif; color: var(--ink); }
  .therapy { position: absolute; left: 22px; top: 247px; font: 600 15.5px "Encode Sans Condensed", sans-serif; color: var(--ink); letter-spacing: .2px; }
  .benefits { position: absolute; left: 22px; top: 270px; list-style: none; }
  .benefits li { display: flex; align-items: center; gap: 4px; font: 400 12px/15.5px "Encode Sans Condensed", sans-serif; color: var(--ink); }
  .benefits svg { width: 8px; height: 8px; flex: none; }
  .follicle-art { position: absolute; left: 305px; top: 225px; width: 36px; height: 150px; border-radius: 18px; background: linear-gradient(180deg, rgba(214,170,96,0) 0%, #d9aa5f 45%, #3a3330 85%); opacity: .8; }
  .site-specific { position: absolute; left: 22px; top: 394px; font: 600 15px "Encode Sans Condensed", sans-serif; color: var(--ink); }
  .count { position: absolute; left: 22px; top: 424px; display: flex; align-items: center; gap: 4px; color: var(--ink); }
  .count .big { font: 600 27px "Fredoka", sans-serif; }
  .count .small { font: 400 9.5px/10px "Encode Sans Condensed", sans-serif; }
  .count .slash { width: 1.5px; height: 30px; background: var(--ink); transform: rotate(14deg); margin: 0 4px; }

  /* Nutrition panel */
  .panel-facts { background: var(--white); }
  .panel-facts .top-rule { position: absolute; left: 0; top: 48px; width: 100%; height: 3px; background: var(--rule); }
  .facts { position: absolute; left: 42px; top: 88px; width: 300px; border: 1px solid var(--ink); padding: 3px 4px; font-family: "Archivo", sans-serif; color: var(--ink); }
  .facts h2 { font: 900 31px/34px "Archivo", sans-serif; letter-spacing: -.5px; border-bottom: 1px solid var(--ink); }
  .facts .row { display: flex; justify-content: space-between; font-size: 8.4px; line-height: 12px; border-bottom: .5px solid #555; }
  .facts .row.thick { border-bottom: 5px solid var(--ink); }
  .facts .row.mid { border-bottom: 2.5px solid var(--ink); }
  .facts .serving { font-weight: 700; font-size: 9px; }
  .facts .cal { font: 900 16px/20px "Archivo", sans-serif; align-items: flex-end; }
  .facts .cal strong { font-size: 19px; }
  .facts .tiny { font-size: 6px; line-height: 9px; }
  .facts .in1 { padding-left: 10px; }
  .facts .in2 { padding-left: 20px; }
  .facts b { font-weight: 700; }
  .facts .note { font-size: 6.2px; line-height: 8px; padding-top: 2px; border: none; }
</style>
</head>
<body>
<div class="label-strip">

  <section class="panel panel-back">
    <div class="top-band"></div>
    <h3 class="back-headline">Headline</h3>
    <p class="back-copy one">Lorem ipsum dolor sit amet, consectetuer adipiscing elit, sed diam nonummy nibh euismod tincidunt ut laoreet dolore magna aliquam erat volutpat. Ut wisi enim ad minim veniam, quis nostrud exerci tation ullamcorper suscipit lobortis nisl ut aliquip ex ea commodo consequat. Duis autem vel eum iriure dolor in hendrerit in vulputate velit esse molestie consequat.</p>
    <p class="back-copy two">Lorem ipsum dolor sit amet, consectetuer adipiscing elit, sed diam nonummy nibh euismod tincidunt ut laoreet dolore magna aliquam erat volutpat. Ut wisi enim ad minim veniam, quis nostrud exerci tation ullamcorper suscipit lobortis nisl ut aliquip ex ea commodo consequat. Duis autem vel eum iriure dolor in hendrerit in vulputate velit esse molestie consequat.</p>
    <div class="info-box"></div>
    <div class="badges">
      <div class="badge"><span class="badge-mark"></span>Gluten Free</div>
      <div class="badge"><span class="badge-mark"></span>Kosher Certified</div>
      <div class="badge"><span class="badge-mark"></span>Lactose Free</div>
      <div class="badge"><span class="badge-mark solid"></span>Non GMO</div>
    </div>
  </section>

  <section class="panel panel-front">
    <svg class="front-shapes" viewBox="0 0 380 470" preserveAspectRatio="none">
      <path d="M0 0 H380 V120 C372 100 360 88 336 86 C316 84 300 90 298 108 C296 122 280 126 260 124 L60 124 C36 124 28 110 20 96 C14 86 6 82 0 84 Z" fill="#ffffff"/>
      <path d="M0 84 C6 82 14 86 20 96 C28 110 36 124 60 124 L260 124 C280 126 296 122 298 108 C300 90 316 84 336 86 C360 88 372 100 380 120" fill="none" stroke="#1d1a18" stroke-width="3"/>
      <path d="M380 120 C352 160 352 220 366 280 C380 340 368 400 330 440 C312 458 296 466 282 470 L380 470 Z" fill="#111"/>
      <path d="M374 140 C346 190 350 250 360 300 C370 350 356 410 318 448" fill="none" stroke="#fff" stroke-width="2" opacity=".6"/>
    </svg>
    <div class="brand"><span class="brand-dot"></span><span class="brand-name">Quillon Health</span></div>
    <div class="eyebrow">GROWTH ACCELERATOR</div>
    <div class="rule" style="top:160px;width:306px"></div>
    <h1 class="product-title">Advanced Women’s<br>Hair Loss Formula</h1>
    <div class="rule" style="top:234px;width:306px"></div>
    <div class="follicle-art" role="img" aria-label="Glowing hair strand and follicle illustration"></div>
    <div class="therapy">TRACTION ALOPECIA THERAPY</div>
    <ul class="benefits">
      <li><svg viewBox="0 0 10 10"><circle cx="5" cy="5" r="4.3" fill="none" stroke="#1d1a18"/><path d="M3 5.2 4.5 6.6 7.2 3.6" fill="none" stroke="#1d1a18" stroke-width="1.2"/></svg>Prevents hair loss &amp; restores thinning, fragile hair</li>
      <li><svg viewBox="0 0 10 10"><circle cx="5" cy="5" r="4.3" fill="none" stroke="#1d1a18"/><path d="M3 5.2 4.5 6.6 7.2 3.6" fill="none" stroke="#1d1a18" stroke-width="1.2"/></svg>Promotes Natural Hair Growth</li>
      <li><svg viewBox="0 0 10 10"><circle cx="5" cy="5" r="4.3" fill="none" stroke="#1d1a18"/><path d="M3 5.2 4.5 6.6 7.2 3.6" fill="none" stroke="#1d1a18" stroke-width="1.2"/></svg>Strengthens Hair for less breakage</li>
      <li><svg viewBox="0 0 10 10"><circle cx="5" cy="5" r="4.3" fill="none" stroke="#1d1a18"/><path d="M3 5.2 4.5 6.6 7.2 3.6" fill="none" stroke="#1d1a18" stroke-width="1.2"/></svg>Visibly increases hair density &amp; thickness</li>
      <li><svg viewBox="0 0 10 10"><circle cx="5" cy="5" r="4.3" fill="none" stroke="#1d1a18"/><path d="M3 5.2 4.5 6.6 7.2 3.6" fill="none" stroke="#1d1a18" stroke-width="1.2"/></svg>Thicker, Stronger, Longer, Hydrated hair</li>
      <li><svg viewBox="0 0 10 10"><circle cx="5" cy="5" r="4.3" fill="none" stroke="#1d1a18"/><path d="M3 5.2 4.5 6.6 7.2 3.6" fill="none" stroke="#1d1a18" stroke-width="1.2"/></svg>Promotes Follicle regeneration &amp; Hair Growth</li>
    </ul>
    <div class="rule" style="top:388px;width:330px"></div>
    <div class="site-specific">Site-Specific for hair loss &amp; stunted growth</div>
    <div class="rule" style="top:416px;width:330px"></div>
    <div class="count">
      <span class="big">60</span><span class="small">capsules</span>
      <span class="slash"></span>
      <span class="big">30</span><span class="small">day<br>supply</span>
    </div>
  </section>

  <section class="panel panel-facts">
    <div class="top-rule"></div>
    <div class="facts">
      <h2>Nutrition Facts</h2>
      <div class="row" style="border:none">4 servings per container/6 raciones por envase</div>
      <div class="row thick serving"><span>Serving size/Tamaño de la porción</span><span>1 cup/1 taza (180g)</span></div>
      <div class="row tiny" style="border:none"><b>Amount per serving/Cantidad por porción</b></div>
      <div class="row mid cal"><span>Calories/Calorías</span><strong>245</strong></div>
      <div class="row tiny" style="justify-content:flex-end"><b>% Daily Value*/% Valor diario*</b></div>
      <div class="row"><span><b>Total Fat/Grasa total</b> 12g</span><b>14%</b></div>
      <div class="row in1"><span>Saturated Fat/Grasa Saturada 2g</span><b>10%</b></div>
      <div class="row in1"><span><i>Trans</i> Fat/Grasa <i>Trans</i> 0g</span></div>
      <div class="row"><span><b>Cholesterol/Colesterol</b> 8mg</span><b>3%</b></div>
      <div class="row"><span><b>Sodium/Sodio</b> 210mg</span><b>9%</b></div>
      <div class="row"><span><b>Total Carbohydrate/Carbohidrato Total</b> 34g</span><b>12%</b></div>
      <div class="row in1"><span>Dietary Fiber/Fibra Dietética 7g</span><b>25%</b></div>
      <div class="row in1"><span>Total Sugars/Azúcares Totales 5g</span></div>
      <div class="row in2"><span>Includes 4g Added Sugars/Incluye 4 g de azúcares añadidos</span><b>8%</b></div>
      <div class="row thick"><span><b>Protein/Proteínas</b> 11g</span></div>
      <div class="row"><span>Vitamin D/Vitamina D 4mcg</span><span>20%</span></div>
      <div class="row"><span>Calcium/Calcio 210mg</span><span>16%</span></div>
      <div class="row"><span>Iron/Hierro 3mg</span><span>15%</span></div>
      <div class="row mid"><span>Potassium/Potasio 380mg</span><span>8%</span></div>
      <div class="row note">* The % Daily Value (DV) tells you how much a nutrient in a serving of food contributes to a daily diet. 2,000 calories a day is used for general nutrition advice.</div>
    </div>
  </section>

</div>
</body>
</html>
```